Super Creative! Pixel Foundry Ad

CREATIVE CREATIVE CREATIVE needed for our Ad that will be placed on Google Ads, in print and on billboards. Our website is https://mypixelfoundry.example

Target Market(s)

B2B

Requirements
Must have
• Uniqueness, creative and the following marks and copy:
1. our logo
2. Our phone number: (555) 274-0386
3. Our website address: mypixelfoundry.example
4. Main message: BUILD BRAND. SUSTAIN GROWTH CURVE.

```html
<!DOCTYPE html>
<html lang="en">
<head>
<meta charset="utf-8">
<title>Pixel Foundry Ad</title>
<link rel="stylesheet" href="https://fonts.googleapis.com/css2?family=Anton&family=Montserrat:wght@700;800&display=swap">
<style>
  :root {
    --page: #0b6396;
    --sky: #33a6e8;
    --sky-deep: #1c86d6;
    --ink: #0b1526;
    --white: #ffffff;
    --accent: #2a8fe0;
    --night: #0c1d3f;
    --night-glow: #1d4f8f;
  }
  * { margin: 0; padding: 0; box-sizing: border-box; }
  html, body { width: 1200px; height: 960px; overflow: hidden; background: var(--page); }
  .ad {
    position: absolute; left: 128px; top: 233px; width: 944px; height: 494px;
    overflow: hidden;
    background: linear-gradient(160deg, var(--sky) 0%, var(--sky-deep) 100%);
    font-family: "Montserrat", Arial, sans-serif;
  }
  .ad__art { position: absolute; inset: 0; }
  .brand {
    position: absolute; left: 26px; top: 34px; height: 68px;
    display: flex; align-items: center; gap: 22px;
  }
  .brand__square { width: 60px; height: 60px; background: var(--ink); }
  .brand__name {
    color: var(--white); font-weight: 700; font-size: 40px;
    letter-spacing: -0.5px; text-transform: uppercase; white-space: nowrap;
  }
  .headline {
    position: absolute; left: 30px; width: 420px; top: 140px;
    text-align: center; font-family: "Anton", Impact, sans-serif;
    font-size: 56px; line-height: 50px; font-weight: 400;
    color: var(--white); text-transform: uppercase;
  }
  .headline__lead { color: var(--ink); display: block; }
  .phone {
    position: absolute; left: 38px; top: 350px;
    display: flex; align-items: center; gap: 10px;
    color: var(--white); font-weight: 700; font-size: 47px; letter-spacing: -1px;
  }
  .phone__icon { width: 48px; height: 48px; }
  .web {
    position: absolute; left: 25px; top: 412px; width: 440px; height: 58px;
    background: var(--ink); color: var(--white);
    display: flex; align-items: center; justify-content: center;
    font-weight: 700; font-size: 31px; text-decoration: none;
  }
  .web__accent { color: var(--accent); }
</style>
</head>
<body>
<main class="ad">
  <svg class="ad__art" width="944" height="494" viewBox="0 0 944 494">
    <defs>
      <linearGradient id="sheen" x1="0" y1="0" x2="0" y2="1">
        <stop offset="0" stop-color="#ffffff" stop-opacity="1"/>
        <stop offset="0.45" stop-color="#ffffff" stop-opacity="0.7"/>
        <stop offset="1" stop-color="#ffffff" stop-opacity="0"/>
      </linearGradient>
      <radialGradient id="photoTone" cx="0.5" cy="0.55" r="0.7">
        <stop offset="0" stop-color="#3fa0ee"/>
        <stop offset="0.35" stop-color="var(--night-glow)"/>
        <stop offset="1" stop-color="var(--night)"/>
      </radialGradient>
    </defs>
    <path class="wave" d="M548 0 H784 L784 87 C760 140 640 150 560 200 C460 260 400 300 300 330 L240 494 H200 L260 320 C380 290 480 260 520 160 C560 90 560 40 548 0 Z" fill="url(#sheen)"/>
    <path class="photo" role="img" aria-label="Photo: a hand touching glowing floating cubes over a dark digital circuit background"
      d="M784 0 H944 V494 H500 C505 380 520 240 576 190 C640 150 770 150 784 87 Z" fill="url(#photoTone)"/>
  </svg>

  <div class="brand">
    <span class="brand__square"></span>
    <span class="brand__name">Pixel Foundry</span>
  </div>

  <h1 class="headline">
    <span class="headline__lead">Build Brand.</span>
    Sustain Growth<br>Curve.
  </h1>

  <div class="phone">
    <svg class="phone__icon" viewBox="0 0 48 48" aria-hidden="true">
      <path d="M12 8 L18 6 L22 16 L17 20 C19 26 23 30 28 32 L32 27 L42 31 L40 38 C38 42 33 43 28 41 C18 37 11 30 7 20 C5 15 7 10 12 8 Z" fill="var(--ink)"/>
      <path d="M27 12 A10 10 0 0 1 36 21 M28 5 A17 17 0 0 1 43 20" fill="none" stroke="var(--ink)" stroke-width="3" stroke-linecap="round"/>
    </svg>
    <span class="phone__number">(555) 274-0386</span>
  </div>

  <a class="web" href="https://mypixelfoundry.example">my<span class="web__accent">pixel</span>foundry.example</a>
</main>
</body>
</html>
```